Letterhead for sustainable Last Mile Logistics needed

Dear all,

we are looking for a powerful design for our letterhead. We are a Berlin-based (Germany) logistics company which delivers parcel on the last mile in a sustainable way. Design should communicate: sustainability, integrity, one family, performance-focused, passionate for excellence and customer experience. Please find company logo attached.

Looking forward for

```html
<!DOCTYPE html>
<html lang="en">
<head>
<meta charset="utf-8">
<title>Linden Freight Letterhead</title>
<link href="https://fonts.googleapis.com/css2?family=Arimo:wght@400&display=swap" rel="stylesheet">
<style>
  :root {
    --brand-green: #138a2c;
    --rule-green: #8ab421;
    --ink: #1c1c1c;
    --paper: #fafafa;
    --backdrop: #ececec;
    --mint-soft: #d4e8dd;
    --lime-soft: #e6efd6;
  }
  * { margin: 0; padding: 0; box-sizing: border-box; }
  html, body {
    width: 1200px; height: 1175px; overflow: hidden;
    background: var(--backdrop);
  }
  .letterhead {
    position: absolute; left: 206px; top: 30px;
    width: 788px; height: 1115px;
    background: var(--paper);
    box-shadow: 0 6px 20px rgba(0,0,0,0.12);
    overflow: hidden;
    font-family: "Arimo", Arial, sans-serif;
    color: var(--ink);
  }
  .brand {
    position: absolute; left: 40px; top: 78px;
    display: flex; align-items: center; gap: 16px;
  }
  .brand-dot {
    width: 70px; height: 70px; border-radius: 50%;
    background: var(--brand-green);
    flex: none;
  }
  .brand-name {
    font-family: "Arimo", Arial, sans-serif;
    font-weight: 400; font-size: 34px; line-height: 1;
    color: var(--brand-green);
    white-space: nowrap;
  }
  .contact {
    position: absolute; left: 482px; top: 54px;
    height: 117px; padding-left: 23px;
    border-left: 1.5px solid var(--rule-green);
    font-size: 14.5px; line-height: 17px;
    font-style: normal;
  }
  .contact-address { margin-bottom: 9px; }
  .contact-row { display: flex; align-items: center; gap: 6px; height: 20px; }
  .contact-row svg { width: 12px; height: 12px; fill: var(--brand-green); flex: none; }
  .letter-body {
    position: absolute; left: 56px; top: 312px; width: 676px;
    font-size: 13.3px; line-height: 20px;
  }
  .salutation { margin-bottom: 17px; }
  .letter-body p.paragraph { text-align: justify; margin-bottom: 19px; }
  .closing { margin-top: 2px; }
  .signature {
    width: 154px; height: 34px; margin: 8px 0 6px;
    background: var(--lime-soft); border-radius: 4px;
  }
  .footer-band {
    position: absolute; left: 353px; right: 0; bottom: 0; height: 122px;
    background: linear-gradient(90deg, var(--mint-soft), var(--lime-soft));
    border-top-left-radius: 122px;
    opacity: 0.8;
  }
</style>
</head>
<body>
<main class="letterhead">
  <header>
    <div class="brand">
      <div class="brand-dot"></div>
      <div class="brand-name">Linden Freight</div>
    </div>
    <address class="contact">
      <div class="contact-address">218 Kastanienallee<br>Floor 2, Berlin, Germany 10435</div>
      <div class="contact-row">
        <svg viewBox="0 0 12 12" aria-hidden="true"><path d="M1 5c0-2 2-3 5-3s5 1 5 3v1H8.5V4.5h-5V6H1z M2.5 7h7l1 4h-9z"/></svg>
        <span>(555) 201 4830</span>
      </div>
      <div class="contact-row">
        <svg viewBox="0 0 12 12" aria-hidden="true"><path d="M3 1h6v3H3z M1 5h10v4H9v2H3V9H1z M4 8v2h4V8z"/></svg>
        <span>(555) 201 4831</span>
      </div>
      <div class="contact-row">
        <svg viewBox="0 0 12 12" aria-hidden="true"><path d="M1 3h10v6H1z"/><path d="M1 3l5 4 5-4" stroke="#fafafa" stroke-width="1" fill="none"/></svg>
        <span>info@lindenfreightgreen.com</span>
      </div>
      <div class="contact-row">
        <svg viewBox="0 0 12 12" aria-hidden="true"><circle cx="6" cy="6" r="5.2"/><path d="M1 6h10M6 1c-2 2-2 8 0 10M6 1c2 2 2 8 0 10" stroke="#fafafa" stroke-width="0.8" fill="none"/></svg>
        <span>www.lindenfreightgreen.com</span>
      </div>
    </address>
  </header>

  <section class="letter-body">
    <p class="salutation">Dear Sir,</p>
    <p class="paragraph">Lorem ipsum dolor sit amet, consectetur adipiscing elit, sed do eiusmod tempor incididunt ut labore et dolore magna aliqua. Ut enim ad minim veniam, quis nostrud exercitation ullamco laboris nisi ut aliquip ex ea commodo consequat. Duis aute irure dolor in reprehenderit in voluptate velit esse cillum dolore eu fugiat nulla pariatur. Excepteur sint occaecat cupidatat non proident, sunt in culpa qui officia deserunt mollit anim id est laborum. It is a long established fact that a reader will be distracted by the readable content of a page when looking at its layout. The point of using Lorem Ipsum is that it has a more-or-less normal distribution of letters, as opposed to using 'Content here, content here', making it look like readable English.</p>
    <p class="paragraph">But I must explain to you how all this mistaken idea of denouncing pleasure and praising pain was born and I will give you a complete account of the system, and expound the actual teachings of the great explorer of the truth, the master-builder of human happiness. No one rejects, dislikes, or avoids pleasure itself, because it is pleasure, but because those who do not know how to pursue pleasure rationally encounter consequences that are extremely painful. Nor again is there anyone who loves or pursues or desires to obtain pain of itself, because it is pain, but because occasionally circumstances occur in which toil and pain can procure him some great pleasure.</p>
    <p class="paragraph">There are many variations of passages of Lorem Ipsum available, but the majority have suffered alteration in some form, by injected humour, or randomised words which don't look even slightly believable. If you are going to use a passage of Lorem Ipsum, you need to be sure there isn't anything embarrassing hidden in the middle of text. All the Lorem Ipsum generators on the Internet tend to repeat predefined chunks as necessary, making this the first true generator on the Internet.</p>
    <p class="closing">Best Regards</p>
    <div class="signature" role="img" aria-label="Handwritten signature of Helen Marsh"></div>
    <p class="signatory">Helen Marsh</p>
  </section>

  <div class="footer-band" aria-hidden="true"></div>
</main>
</body>
</html>
```